Maple Lantern Business Card

Design of business cards

Target Market(s)

We are aiming as small business owners who need anything from basic business structures, website plans, business processes and quality assurance.

Industry/Entity Type

Business

Colors

Designer to choose colors to be used in the design.

Requirements
Nice to have
• I would prefer one side of the card to use the green from the logo. Prefer to have the same font as the logo.

```html
<!DOCTYPE html>
<html lang="en">
<head>
<meta charset="utf-8">
<title>Maple Lantern Consulting – Business Cards</title>
<link rel="stylesheet" href="https://fonts.googleapis.com/css2?family=Cinzel:wght@400;500;600&display=swap">
<style>
  :root {
    --leaf: #a6ce39;
    --slate: #58585a;
    --paper: #f7f8f8;
    --edge: #d7d8d8;
    --white: #ffffff;
  }
  * { margin: 0; padding: 0; box-sizing: border-box; }
  html, body { width: 1006px; height: 1200px; overflow: hidden; background: var(--white); }
  body { position: relative; font-family: "Cinzel", "Times New Roman", serif; }

  .card {
    position: absolute;
    left: 94px;
    width: 815px;
    background: var(--paper);
    border: 2px solid var(--edge);
    overflow: hidden;
  }
  .card--front { top: 62px; height: 526px; }
  .card--back  { top: 617px; height: 532px; }

  .brand {
    position: absolute;
    display: flex;
    align-items: center;
    gap: 34px;
  }
  .card--front .brand { left: 258px; top: 192px; }
  .card--back  .brand { left: 258px; top: 650px; top: 34px; }
  .brand__mark {
    width: 100px; height: 100px;
    border-radius: 50%;
    background: var(--leaf);
    flex: none;
  }
  .brand__name {
    color: var(--leaf);
    font-weight: 500;
    font-size: 34px;
    line-height: 48px;
    letter-spacing: 1px;
  }

  .front-band {
    position: absolute;
    left: 0; right: 0; top: 417px; bottom: 0;
    background: var(--slate);
    border-top: 6px solid var(--leaf);
  }

  .back-panel {
    position: absolute;
    left: 0; right: 0; top: 212px; bottom: 0;
    background: var(--leaf);
    border-top: 9px solid var(--slate);
  }

  .holder {
    position: absolute;
    left: 0; right: 0; top: 290px;
    text-align: center;
    color: var(--white);
    font-size: 58px;
    font-weight: 500;
    letter-spacing: 2px;
  }

  .contact {
    position: absolute;
    left: 34px; right: 34px;
    display: flex;
    justify-content: space-between;
    align-items: center;
    color: var(--white);
    font-size: 24px;
    font-weight: 500;
  }
  .card--front .contact { top: 437px; }
  .card--back  .contact { top: 465px; }
  .contact__phone { display: flex; align-items: center; gap: 12px; }
  .contact__icon { width: 36px; height: 36px; flex: none; }
  .contact__web { letter-spacing: 1px; }
</style>
</head>
<body>

  <section class="card card--front" aria-label="Card front">
    <div class="brand">
      <span class="brand__mark" aria-hidden="true"></span>
      <p class="brand__name">Maple Lantern<br>Consulting</p>
    </div>
    <div class="front-band"></div>
    <div class="contact">
      <span class="contact__phone">
        <svg class="contact__icon" viewBox="0 0 36 36" aria-hidden="true">
          <circle cx="18" cy="18" r="16" fill="none" stroke="#fff" stroke-width="2.5"/>
          <path d="M12 10c1.2-1 2.6-.8 3.2.4l1.4 2.8c.5 1 .2 2-.7 2.6l-1 .7c.8 2 2.4 3.6 4.4 4.6l.8-1c.6-.9 1.7-1.1 2.6-.6l2.8 1.5c1.2.6 1.3 2 .3 3.1-1.6 1.8-4 2.2-6.6.9-3.5-1.7-6.6-4.9-8.1-8.4-1.1-2.6-.8-5 .9-6.6z" fill="#fff"/>
        </svg>
        000-111-222
      </span>
      <span class="contact__web">www.(yourwebsite).com</span>
    </div>
  </section>

  <section class="card card--back" aria-label="Card back">
    <div class="brand">
      <span class="brand__mark" aria-hidden="true"></span>
      <p class="brand__name">Maple Lantern<br>Consulting</p>
    </div>
    <div class="back-panel"></div>
    <h1 class="holder">Daniel Verhoven</h1>
    <div class="contact">
      <span class="contact__phone">
        <svg class="contact__icon" viewBox="0 0 36 36" aria-hidden="true">
          <circle cx="18" cy="18" r="16" fill="none" stroke="#fff" stroke-width="2.5"/>
          <path d="M12 10c1.2-1 2.6-.8 3.2.4l1.4 2.8c.5 1 .2 2-.7 2.6l-1 .7c.8 2 2.4 3.6 4.4 4.6l.8-1c.6-.9 1.7-1.1 2.6-.6l2.8 1.5c1.2.6 1.3 2 .3 3.1-1.6 1.8-4 2.2-6.6.9-3.5-1.7-6.6-4.9-8.1-8.4-1.1-2.6-.8-5 .9-6.6z" fill="#fff"/>
        </svg>
        000-111-222
      </span>
      <span class="contact__web">www.(yourwebsite).com</span>
    </div>
  </section>

</body>
</html>
```